Visitenkarten-Design für Forschungs- und Beratungsunternehmen
Zielgruppe
*Veloricum' ist ein Forschungs- und Beratungsunternehmen für Lebensmittelwirkungen. Unsere Angebote sind: Vorträge, Workshops, Seminare und Coaching. Die Zielgruppen sind Pädagogen, Mediziner, Psychologen u.a.m.
Aufgabenstellung
Bei Bedarf kann die Gestaltung der Visitenkarte auch auf die Rückseite ausgedehnt werden.

```html
<!DOCTYPE html>
<html lang="de">
<head>
<meta charset="utf-8">
<title>Veloricum – Visitenkarte</title>
<link href="https://fonts.googleapis.com/css2?family=Open+Sans:wght@400;600;700&display=swap" rel="stylesheet">
<style>
  :root {
    --stage: #2a2a2c;
    --card: #1c1c1e;
    --card-edge: #111113;
    --ink: #f2f2f2;
    --ink-soft: #c9c9c9;
    --silver-light: #f4f4f4;
    --silver-mid: #b8b8bc;
    --silver-dark: #6e6e72;
  }
  * { margin: 0; padding: 0; box-sizing: border-box; }
  html, body { width: 1200px; height: 901px; overflow: hidden; }
  body {
    background: var(--stage);
    font-family: "Open Sans", Arial, sans-serif;
    color: var(--ink);
    position: relative;
  }
  .card {
    position: absolute;
    left: 300px;
    width: 600px;
    height: 343px;
    background: var(--card);
    border: 1px solid var(--card-edge);
    overflow: hidden;
    box-shadow: 0 18px 40px rgba(0,0,0,.45);
  }
  .card--front { top: 90px; }
  .card--back { top: 468px; }
  .card__band { position: absolute; left: 0; top: 0; width: 600px; height: 343px; }

  .brand {
    position: absolute;
    display: flex;
    align-items: center;
    gap: 10px;
    font-weight: 700;
    color: var(--ink);
    letter-spacing: .02em;
  }
  .brand__dot {
    width: 14px; height: 14px; border-radius: 50%;
    background: var(--ink);
  }
  .card--front .brand { right: 60px; top: 62px; font-size: 26px; }
  .card--back .brand { left: 50%; top: 140px; transform: translateX(-50%); font-size: 38px; }
  .card--back .brand__dot { width: 18px; height: 18px; }

  .website {
    position: absolute;
    font-size: 14px;
    font-weight: 600;
    color: var(--ink);
  }
  .card--front .website { right: 22px; top: 132px; }
  .card--back .website { right: 40px; bottom: 22px; color: #2b2b2e; }

  .person { position: absolute; left: 46px; top: 130px; }
  .person__name { font-size: 19px; font-weight: 600; line-height: 1.2; }
  .person__role { font-size: 13px; color: var(--ink-soft); }

  .contact { position: absolute; left: 46px; bottom: 28px; list-style: none; }
  .contact__item {
    display: flex; align-items: center; gap: 10px;
    font-size: 14px; line-height: 21px; color: var(--ink);
  }
  .contact__icon { width: 12px; height: 12px; fill: var(--ink); }
</style>
</head>
<body>

<section class="card card--front" aria-label="Vorderseite">
  <svg class="card__band" viewBox="0 0 600 343" aria-hidden="true">
    <defs>
      <linearGradient id="silver-top" x1="0" y1="0" x2="1" y2="0">
        <stop offset="0" stop-color="var(--silver-dark)"/>
        <stop offset=".45" stop-color="var(--silver-light)"/>
        <stop offset="1" stop-color="var(--silver-mid)"/>
      </linearGradient>
    </defs>
    <path d="M170 0 H600 V12 H215 Q200 12 192 20 L180 30 Q172 36 160 36 H0 V30 H150 Q162 30 168 22 Z" fill="url(#silver-top)"/>
    <path d="M0 0 H170 L168 22 Q162 30 150 30 H0 Z" fill="var(--card)"/>
    <path d="M330 212 Q342 200 358 200 H600 V210 H362 Q348 210 340 222 L334 230 Q328 236 316 236 H0 V232 H312 Q322 232 330 212 Z" fill="url(#silver-top)" opacity=".9"/>
  </svg>

  <div class="brand"><span class="brand__dot"></span>Veloricum</div>
  <p class="website">www.veloricum.ch</p>

  <div class="person">
    <p class="person__name">Mathis Lindauer</p>
    <p class="person__role">Director</p>
  </div>

  <ul class="contact">
    <li class="contact__item">
      <svg class="contact__icon" viewBox="0 0 12 12" aria-hidden="true"><path d="M2.5 0.5 L4.5 3 L3.3 4.3 Q4.3 6.8 7.7 8.7 L9 7.5 L11.5 9.5 L10 11.5 Q4.5 11 0.5 2 Z"/></svg>
      +41 61 555 24 80
    </li>
    <li class="contact__item">
      <svg class="contact__icon" viewBox="0 0 12 12" aria-hidden="true"><path d="M0 2 H12 V10 H0 Z M1 3 L6 6.5 L11 3 V3.2 L6 7.6 L1 3.2 Z" fill-rule="evenodd"/></svg>
      info@veloricum.ch
    </li>
    <li class="contact__item">
      <svg class="contact__icon" viewBox="0 0 12 12" aria-hidden="true"><path d="M6 0 A4 4 0 0 1 10 4 Q10 7 6 12 Q2 7 2 4 A4 4 0 0 1 6 0 Z M6 2.5 A1.5 1.5 0 1 0 6 5.5 A1.5 1.5 0 1 0 6 2.5 Z" fill-rule="evenodd"/></svg>
      CH-4999 Waldmatt
    </li>
  </ul>
</section>

<section class="card card--back" aria-label="Rückseite">
  <svg class="card__band" viewBox="0 0 600 343" aria-hidden="true">
    <defs>
      <linearGradient id="silver-bottom" x1="0" y1="0" x2="1" y2="0">
        <stop offset="0" stop-color="var(--silver-mid)"/>
        <stop offset=".5" stop-color="var(--silver-light)"/>
        <stop offset="1" stop-color="var(--silver-mid)"/>
      </linearGradient>
    </defs>
    <path d="M0 331 H290 Q308 331 320 318 Q332 303 352 303 H600 V343 H0 Z" fill="url(#silver-bottom)"/>
  </svg>

  <div class="brand"><span class="brand__dot"></span>Veloricum</div>
  <p class="website">www.veloricum-forschung.ch</p>
</section>

</body>
</html>
```